Need Stunning Website for Talent Acquisition (Recruiting) Agency

Hello, I am seeking a very professional, high-quality website that reflects our Talent Acquisition agency, Cobalt Kin. Our agency slogan is "Talent Acquisition. Differently." We are in fact different - we are a full service agency that provides services most others do not, and our website needs to immediately reflect that something is different about us when they visit our site.

This contest is to do complete website design and coding, including all graphics, features, plugins, and design elements. The graphics are very important on the site and must be of the highest professional quality. One critical aspect is that the imagery must convey that we serve clients in a variety of industries, including business, healthcare, churches and religious organizations, non-profits, manufacturing, retail, and more. We recruit for both professional level positions (e.g. CEO, COO, Pastor), as well as entry level (e.g. secretary, caregiver, factory worker).
The following pages should be designed:
Home Page - a captivating home page that immediately tells our brand story, what makes us different, and the value that we bring to the table.
Client Services Page - a page that talks more about the services we provide and why we produce better results. This page will cover the 5 C's in greater detail as well as all the things that make us different.
Industries - The industries we serve
Request Services - a page where clients can submit details about a job they would like us to recruit for, including attaching a job description if they have one
Candidates Page - a simple page that encourages prospective candidates to submit their resume for review
About Us - Common about us page
Blog - Common blog page
Contact Us - a contact page for general inquiries
The website must be built in an ultra-SEO friendly manner and optimized for speed and performance. As mentioned above, you will be responsible for providing all graphics for the site (copyright compliant).
The website will need to be compatible with Elementor Pro (I have subscription) and Yoast SEO. It needs to be designed on a high-quality wordpress theme that receives regular updates. It also needs instant chat messaging feature. Would like a traditional menu bar at the top of the page (not a fan of menu's that are hidden or put on the side of the page).

Please, please, please - - do NOT waste my time with generic/stock templates, low-quality graphics, etc. We are a PREMIUM agency and our website needs to reflect that.

In the future we will add a job board - I do not want that initially - but will want the option to add it later.

Must also have the ability to upload documents /attachments on the contact page/form.

It probably goes without saying, but the page must be fully responsive - suitable to work on all device types.

Target Market(s)

Businesses

Industry/Entity Type

Talent Acquisition (Recruiting) Agency

Coding

Coded - Design and coding required

Number of Pages Required

5+ page

Requirements
Must have
• Please see brief
Should not have
• No generic template/stock website or graphics - must have PREMIUM feel.

```html
<!DOCTYPE html>
<html lang="en">
<head>
<meta charset="utf-8">
<title>Cobalt Kin — Talent Acquisition. Differently</title>
<link rel="stylesheet" href="https://fonts.googleapis.com/css2?family=Poppins:wght@400;500;600&display=swap">
<style>
  :root {
    --navy: #131d4b;
    --amber: #fba900;
    --ink: #111111;
    --icon-grey: #c8c8c8;
    --photo-light: #a48d87;
    --photo-dark: #7a6561;
    --white: #ffffff;
  }
  * { margin: 0; padding: 0; box-sizing: border-box; }
  html, body { width: 1200px; height: 1059px; overflow: hidden; background: var(--white); }
  body { font-family: "Poppins", sans-serif; color: var(--ink); position: relative; }

  .site-header { position: absolute; left: 0; top: 0; width: 1200px; height: 80px; }
  .brand { position: absolute; left: 135px; top: 22px; font-weight: 600; font-size: 25px; color: var(--navy); letter-spacing: -0.5px; }
  .main-nav { position: absolute; left: 540px; top: 31px; display: flex; }
  .main-nav a { font-size: 14px; font-weight: 500; color: var(--ink); text-decoration: none; margin-right: 28px; line-height: 20px; }
  .btn { display: inline-flex; align-items: center; justify-content: center; background: var(--navy); color: var(--white); font-weight: 500; text-decoration: none; border-radius: 9px; }
  .btn-header { position: absolute; left: 931px; top: 21px; width: 133px; height: 38px; font-size: 15px; border-radius: 6px; }

  .hero-title { position: absolute; left: 134px; top: 178px; font-size: 63px; font-weight: 600; color: var(--navy); letter-spacing: -0.5px; line-height: 80px; }
  .hero-tagline { position: absolute; left: 135px; top: 263px; font-size: 33px; font-weight: 600; color: var(--amber); line-height: 42px; letter-spacing: -0.6px; white-space: nowrap; }
  .hero-copy { position: absolute; left: 135px; top: 363px; width: 360px; font-size: 14px; line-height: 20px; }
  .btn-hero { position: absolute; left: 136px; top: 468px; width: 117px; height: 43px; font-size: 15px; }

  .hero-blob { position: absolute; left: 575px; top: 190px; width: 495px; height: 490px; }
  .hero-photo { position: absolute; left: 690px; top: 117px; width: 300px; height: 561px; border-radius: 150px 150px 0 0; background: linear-gradient(180deg, var(--photo-light), var(--photo-dark)); }

  .serve-title { position: absolute; left: 0; top: 742px; width: 1188px; text-align: center; font-size: 42px; font-weight: 600; color: var(--navy); line-height: 56px; }
  .serve-copy { position: absolute; left: 250px; top: 808px; width: 700px; text-align: center; font-size: 14px; line-height: 20px; }

  .industry-icons { position: absolute; left: 0; top: 893px; width: 1200px; height: 106px; }
  .industry-icon { position: absolute; top: 0; width: 106px; height: 106px; }
  .industry-icon svg { width: 106px; height: 106px; fill: none; stroke: var(--icon-grey); stroke-width: 3.5; stroke-linejoin: round; stroke-linecap: round; }

  .footer-band { position: absolute; left: 0; bottom: 0; width: 1200px; height: 6px; background: var(--navy); }
</style>
</head>
<body>
  <header class="site-header">
    <div class="brand">Cobalt Kin</div>
    <nav class="main-nav">
      <a href="#">Home</a>
      <a href="#">Services</a>
      <a href="#">Industries</a>
      <a href="#">About us</a>
      <a href="#">Blog</a>
    </nav>
    <a class="btn btn-header" href="#">Get Started</a>
  </header>

  <section class="hero">
    <h1 class="hero-title">Cobaltkin</h1>
    <p class="hero-tagline">TALENT ACQUISITION.<br>DIFFERENTLY</p>
    <p class="hero-copy">"Lorem ipsum dolor sit amet, consectetur adipiscing elit, sed do eiusmod tempor incididunt ut labore et dolore magna aliqua. Ut enim ad minim veniam, quis nostrud exercitation ullamco</p>
    <a class="btn btn-hero" href="#">Get Started</a>

    <svg class="hero-blob" viewBox="0 0 495 490" aria-hidden="true">
      <path fill="var(--amber)" d="M206 39 C250 10 300 5 341 12 C420 40 487 100 487 174 C487 250 445 290 435 338 C425 390 415 450 408 488 L153 488 C90 455 6 410 6 327 C6 260 90 230 129 174 C160 120 180 60 206 39 Z"/>
    </svg>
    <div class="hero-photo" role="img" aria-label="Smiling young professional in glasses and a checked blazer, arms crossed"></div>
  </section>

  <section class="we-serve">
    <h2 class="serve-title">We Serve</h2>
    <p class="serve-copy">"Lorem ipsum dolor sit amet, consectetur adipiscing elit, sed do eiusmod tempor incididunt ut labore et dolore magna aliqua. Ut enim ad minim veniam, quis nostrud exercitation ullamco</p>

    <div class="industry-icons">
      <div class="industry-icon" style="left:152px" aria-label="Business">
        <svg viewBox="0 0 100 100"><circle cx="50" cy="28" r="22" stroke-dasharray="6 4"/><circle cx="50" cy="24" r="8"/><path d="M36 46 C36 36 64 36 64 46"/><path d="M4 52 L20 48 L24 76 L6 78 Z"/><path d="M96 52 L80 48 L76 76 L94 78 Z"/><path d="M22 54 L44 54 L58 62 L52 68 L42 62"/><path d="M78 56 L60 58 L26 72 L40 90 L56 96 L70 84 L78 78"/><path d="M34 78 L42 86 M40 74 L48 82 M46 70 L54 78"/></svg>
      </div>
      <div class="industry-icon" style="left:351px" aria-label="Healthcare">
        <svg viewBox="0 0 100 100"><path d="M50 54 C30 40 22 32 22 20 C22 10 30 4 38 4 C44 4 48 8 50 12 C52 8 56 4 62 4 C70 4 78 10 78 20 C78 32 70 40 50 54 Z"/><path d="M50 20 V34 M43 27 H57"/><path d="M8 40 C4 60 14 78 30 88 L40 96 L40 84 C40 74 34 68 26 60 L18 52"/><path d="M92 40 C96 60 86 78 70 88 L60 96 L60 84 C60 74 66 68 74 60 L82 52"/><path d="M40 96 H60"/></svg>
      </div>
      <div class="industry-icon" style="left:547px" aria-label="Non-profit">
        <svg viewBox="0 0 100 100"><path d="M2 42 L50 4 L98 42"/><path d="M10 36 V96 H90 V36"/><path d="M50 40 C42 34 38 30 38 24 C38 19 42 16 46 16 C48 16 50 18 50 20 C50 18 52 16 54 16 C58 16 62 19 62 24 C62 30 58 34 50 40 Z"/><path d="M26 78 L40 64 L58 64 C62 64 62 70 58 70 L48 70 M58 70 L70 62 C74 60 78 64 74 68 L60 80 L38 80 L30 86"/></svg>
      </div>
      <div class="industry-icon" style="left:744px" aria-label="Manufacturing">
        <svg viewBox="0 0 100 100"><circle cx="50" cy="28" r="22" stroke-dasharray="6 4"/><circle cx="50" cy="24" r="8"/><path d="M36 46 C36 36 64 36 64 46"/><path d="M4 52 L20 48 L24 76 L6 78 Z"/><path d="M96 52 L80 48 L76 76 L94 78 Z"/><path d="M22 54 L44 54 L58 62 L52 68 L42 62"/><path d="M78 56 L60 58 L26 72 L40 90 L56 96 L70 84 L78 78"/><path d="M34 78 L42 86 M40 74 L48 82 M46 70 L54 78"/></svg>
      </div>
      <div class="industry-icon" style="left:941px" aria-label="Churches and religious organisations">
        <svg viewBox="0 0 100 100"><path d="M50 54 C30 40 22 32 22 20 C22 10 30 4 38 4 C44 4 48 8 50 12 C52 8 56 4 62 4 C70 4 78 10 78 20 C78 32 70 40 50 54 Z"/><path d="M50 20 V34 M43 27 H57"/><path d="M8 40 C4 60 14 78 30 88 L40 96 L40 84 C40 74 34 68 26 60 L18 52"/><path d="M92 40 C96 60 86 78 70 88 L60 96 L60 84 C60 74 66 68 74 60 L82 52"/><path d="M40 96 H60"/></svg>
      </div>
    </div>
  </section>

  <div class="footer-band"></div>
</body>
</html>
```